Acai Bowl and Coffee Van need new Menus

We currently have a basic menu that is displayed in an A3 frame. It lacks images, specifically of the Acai Bowls and is difficult to read and understand.

We need a new Acai Bowl Menu and a new Drink Menu but in a more attractive and easier to read format.
We would like images of the Acai Bowls (using Images supplied or make your own) in order to show customers what is on each bowl. Customers chose what granola they would like from the three that are available. Currently we tell customers to check the bottom of the menu as they are often unaware they get to chose.

The drink menu items are simple (we have removed smoothies from our menu entirely).
The drink menu needs to have "Chai Latte" and "Dirty Chai Latte" added as options with the same S,M,L pricing as a Latte.

I have attached images of the menus and a photo of how the menus are displayed on The Brindle Cart. Also attached is photos of the Acai Bowls and other food / drink items on the menu if you wish to use them in your design. I have included the files for all of our logo variations.

Our main objective with the menu redesign is to have the menu more appealing and easier to read and understand.

Industry/Entity Type

Food and Coffee

Font styles to use
Other font styles liked:
• Orplid Pro (Fill and Shadow), Trend Sans One

Colors

Designer to choose colors to be used in the design.

Requirements
Must have
• The final design must include prices and be editable in the case of any price changes in the future.

```html
<!DOCTYPE html>
<html lang="en">
<head>
<meta charset="utf-8">
<title>Acai Bowls Menu – The Brindle Cart</title>
<link rel="stylesheet" href="https://fonts.googleapis.com/css2?family=Exo+2:wght@300;400;500&display=swap">
<style>
  :root {
    --backdrop: #b4b1b2;
    --menu-pink: #f1e1e3;
    --menu-pink-deep: #eedcdf;
    --tan: #b39a6e;
    --ink: #1d1a1a;
    --white: #ffffff;
    --cream: #ece3d8;
    --caramel: #e3ad6a;
    --cocoa: #3a2418;
  }
  * { box-sizing: border-box; margin: 0; padding: 0; }
  html, body {
    width: 1200px; height: 1200px; overflow: hidden;
    background: var(--backdrop);
  }
  .menu {
    position: absolute;
    left: 233px; top: 80px;
    width: 735px; height: 1040px;
    background: linear-gradient(180deg, var(--menu-pink) 0%, var(--menu-pink-deep) 100%);
    box-shadow: 4px 6px 10px rgba(60, 50, 50, 0.35);
    overflow: hidden;
    font-family: "Exo 2", sans-serif;
  }
  .menu__photo {
    position: absolute; left: 0; top: 0;
    width: 735px; height: 600px;
    background:
      radial-gradient(ellipse 34% 13% at 48% 30%, rgba(58,36,24,0.9) 0%, rgba(58,36,24,0.6) 50%, rgba(58,36,24,0) 100%),
      radial-gradient(ellipse 26% 9% at 68% 44%, rgba(58,36,24,0.75) 0%, rgba(58,36,24,0) 100%),
      radial-gradient(ellipse 38% 7% at 50% 40%, rgba(227,173,106,0.7) 0%, rgba(227,173,106,0) 100%),
      linear-gradient(180deg, #ddd2c6 0%, var(--cream) 55%, rgba(241,225,227,0.7) 82%, var(--menu-pink) 100%);
  }
  .menu__title {
    position: absolute; left: 0; top: 452px; width: 100%;
    text-align: center;
    font-weight: 300;
    font-size: 104px;
    letter-spacing: -1px;
    line-height: 1.1;
    color: var(--white);
    text-shadow:
      1.5px 0 0 var(--tan), -1.5px 0 0 var(--tan),
      0 1.5px 0 var(--tan), 0 -1.5px 0 var(--tan),
      1px 1px 0 var(--tan), -1px -1px 0 var(--tan),
      1px -1px 0 var(--tan), -1px 1px 0 var(--tan),
      4px 5px 5px rgba(90, 70, 50, 0.55);
  }
  .menu__items {
    position: absolute; left: 45px; top: 598px;
    width: 640px;
    list-style: none;
  }
  .menu-item {
    display: flex; justify-content: space-between;
    height: 57.5px;
    color: var(--ink);
    font-size: 15px; line-height: 19px;
  }
  .menu-item__price { width: 55px; font-size: 16px; }
  .menu__brand {
    position: absolute; right: 54px; top: 912px;
    font-weight: 500;
    font-size: 30px;
    line-height: 40px;
    color: var(--tan);
    letter-spacing: 0.5px;
  }
  .menu__decor { position: absolute; left: 0; top: 0; }
</style>
</head>
<body>
  <main class="menu">
    <div class="menu__photo" role="img" aria-label="Photo of two chocolate and caramel slices topped with crushed nuts on a pale wooden surface"></div>

    <h1 class="menu__title">ACAI BOWLS</h1>

    <ul class="menu__items">
      <li class="menu-item"><span class="menu-item__desc">Lorem Ipsum is simply dummy text of the printing and typesetting industry<br>Lorem Ipsum is simply dummy text</span><span class="menu-item__price">$27</span></li>
      <li class="menu-item"><span class="menu-item__desc">Lorem Ipsum is simply dummy text of the printing and typesetting industry<br>Lorem Ipsum is simply dummy text</span><span class="menu-item__price">$27</span></li>
      <li class="menu-item"><span class="menu-item__desc">Lorem Ipsum is simply dummy text of the printing and typesetting industry<br>Lorem Ipsum is simply dummy text</span><span class="menu-item__price">$27</span></li>
      <li class="menu-item"><span class="menu-item__desc">Lorem Ipsum is simply dummy text of the printing and typesetting industry<br>Lorem Ipsum is simply dummy text</span><span class="menu-item__price">$27</span></li>
      <li class="menu-item"><span class="menu-item__desc">Lorem Ipsum is simply dummy text of the printing and typesetting industry<br>Lorem Ipsum is simply dummy text</span><span class="menu-item__price">$27</span></li>
    </ul>

    <p class="menu__brand">The Brindle Cart</p>

    <svg class="menu__decor" width="735" height="1040" viewBox="0 0 735 1040" aria-hidden="true">
      <path d="M0 920 C 35 924, 44 960, 52 985 C 64 1022, 110 1012, 142 1040" fill="none" stroke="var(--tan)" stroke-width="2.5"/>
      <g fill="var(--tan)">
        <polygon points="150,984 165,976 165,992"/>
        <polygon points="182,984 197,976 197,992"/>
        <polygon points="214,984 229,976 229,992"/>
        <polygon points="246,984 261,976 261,992"/>
        <polygon points="278,984 293,976 293,992"/>
      </g>
    </svg>
  </main>
</body>
</html>
```